New homepage design - Summit Mentors

- we would like to have a new website layout of the existing one: www.summitmentors-example.ch
the new layout should have the following parameters:
- we want it to be minimalistic
- clear lines
- not too colourful (eventually also more in grey tone?)

our company: summit mentors
- summit mentors is an organizational consulting company and we work with organizations and individuals alike
- we are headquartered in the engadine
- examples: www.bramblequay-example.nyc, www.tallowandfern-example.com, www.corvenhaze-example.com, www.pelldriscoll-example.website,

Target Market(s)

Companies

Industry/Entity Type

Consulting

Number of Pages Required

1 page

Font styles to use
Sans Serif

Colors

Designer to choose only greyscale colors for use in the design.

Requirements
Must have
• A minimalistic design
Nice to have
• minimalistic and slick
Should not have
• not too many colours

```html
<!DOCTYPE html>
<html lang="en">
<head>
<meta charset="utf-8">
<title>Summit Mentors – Turn growth into thriving</title>
<link href="https://fonts.googleapis.com/css2?family=DM+Sans:wght@300;400;500;600&display=swap" rel="stylesheet">
<style>
:root{
  --ink:#111111;
  --text:#333333;
  --muted:#7a7a7a;
  --light:#dedede;
  --white:#ffffff;
  --black:#000000;
  --card-shadow:0 4px 18px rgba(0,0,0,.08);
}
*{margin:0;padding:0;box-sizing:border-box}
html,body{width:1200px;height:5023px;overflow:hidden}
body{font-family:'DM Sans',Arial,sans-serif;color:var(--text);background:var(--white);position:relative}
section,header,footer{position:absolute;left:0;width:1200px}
.abs{position:absolute}
a{color:inherit;text-decoration:none}
.link-underline{font-size:15px;font-weight:500;color:var(--ink);padding-bottom:8px;border-bottom:2px solid var(--ink);display:inline-block}

/* header */
.site-header{top:0;height:142px;background:var(--white);z-index:3}
.brand-box{left:84px;top:0;width:279px;height:187px;background:var(--white);display:flex;align-items:flex-end;justify-content:center;padding-bottom:42px;z-index:4}
.brand-name{font-size:27px;font-weight:300;letter-spacing:1px;color:var(--ink)}
.main-nav{left:382px;top:58px;display:flex;gap:26px;font-size:15px;font-weight:500;color:var(--ink)}
.main-nav span::after{content:" ▾";font-size:10px}
.contact-btn{left:997px;top:47px;width:113px;height:45px;background:var(--black);color:var(--white);font-size:15px;font-weight:500;display:flex;align-items:center;justify-content:center}

/* hero */
.hero{top:142px;height:592px;background:linear-gradient(90deg,#000 0%,#0a0a0a 38%,#3a3a3a 62%,#8a8a8a 78%,#4a4a4a 100%)}
.hero-title{left:86px;top:108px;font-size:56px;font-weight:500;line-height:68px;color:var(--white);width:620px}
.hero .link-underline{position:absolute;left:86px;top:440px;color:var(--white);border-color:var(--white)}

/* section headings */
.section-title{width:100%;text-align:center;font-size:38px;font-weight:500;color:var(--ink)}
.section-sub{width:100%;text-align:center;font-size:13px;line-height:21px;color:var(--muted)}

/* why & how */
.why{top:734px;height:710px}
.why .section-title{top:96px}
.why .section-sub{top:152px}
.feature-card{top:228px;width:500px;height:376px;color:var(--white);padding:44px 46px}
.feature-card h3{font-size:27px;font-weight:400}
.feature-card p{position:absolute;left:46px;bottom:52px;width:320px;font-size:13px;line-height:21px}
.arrow-btn{position:absolute;right:46px;bottom:52px;width:46px;height:46px;border:2px solid var(--white);border-radius:50%;display:flex;align-items:center;justify-content:center}
.card-why{left:86px;background:linear-gradient(135deg,#4a4546,#3c3a3b 60%,#2c2b2b)}
.card-how{left:613px;background:linear-gradient(160deg,#5a5652,#2a2826 55%,#161514)}

/* retreats */
.retreats{top:1444px;height:1008px;background:var(--light)}
.retreats-title{left:0;top:94px;width:100%;text-align:center}
.retreats-title span{font-size:27px;font-weight:400;color:var(--ink);padding-bottom:12px;border-bottom:3px solid var(--ink)}
.retreat-image{left:86px;top:181px;width:1028px;height:379px;background:linear-gradient(180deg,#cfd2d3 0%,#6d746c 30%,#2a3028 45%,#b8bcbc 58%,#8b8f88 80%,#6a6556 100%)}
.retreats .read-more{left:0;top:591px;width:100%;text-align:center}
.retreats .section-title{top:690px}
.intro-copy{left:180px;top:752px;width:840px;text-align:center;font-size:13px;line-height:21px;color:var(--muted)}
.intro-copy p{margin-bottom:10px}

/* team */
.team{top:2452px;height:672px}
.team-title{left:86px;top:98px;font-size:38px;font-weight:500;color:var(--ink)}
.team-note{left:560px;top:104px;width:560px;font-size:13px;line-height:21px;color:var(--muted)}
.member{top:176px;width:324px;height:394px;background:linear-gradient(180deg,#7fa6cf 0%,#6c8fb8 45%,#2d3646 80%,#1c222c 100%)}
.member .role{position:absolute;left:22px;bottom:58px;font-size:13px;color:var(--white)}
.member .name{position:absolute;left:22px;bottom:30px;font-size:19px;font-weight:500;color:var(--white)}
.member-icons{position:absolute;right:10px;top:14px;display:flex;flex-direction:column;gap:20px}
.member-icons span{width:36px;height:36px;background:#e6e6e6;display:flex;align-items:center;justify-content:center}

/* testimonials */
.testimonials{top:3124px;height:593px;background:var(--light)}
.testimonials .section-title{top:94px}
.quote-card{top:169px;width:500px;height:318px;background:var(--white);box-shadow:var(--card-shadow);padding:50px 40px 0}
.quote-card p{font-size:15px;line-height:23px;color:var(--muted)}
.quote-author{position:absolute;left:40px;top:228px;font-size:19px;font-weight:500;color:var(--ink)}
.quote-role{position:absolute;left:40px;top:258px;font-size:13px;color:var(--muted)}
.partner-name{position:absolute;right:40px;top:236px;font-size:24px;font-weight:600;color:var(--ink)}

/* media */
.media{top:3717px;height:786px}
.media .section-title{top:98px}
.media .section-sub{top:162px}
.press-card{top:228px;width:324px;height:455px;background:var(--white);box-shadow:var(--card-shadow)}
.press-image{position:absolute;left:0;top:0;width:324px;height:252px}
.press-date{position:absolute;left:36px;top:228px;background:var(--white);font-size:12px;color:var(--muted);padding:6px 16px}
.press-card h4{position:absolute;left:36px;top:290px;width:260px;font-size:21px;font-weight:500;line-height:29px;color:var(--ink)}
.press-card .link-underline{position:absolute;left:36px;top:392px}

/* footer */
.site-footer{top:4503px;height:520px;background:var(--black);color:var(--white)}
.footer-brand{left:86px;top:166px;font-size:27px;font-weight:300;letter-spacing:1px;color:#9a9a9a}
.footer-social{left:86px;top:229px;display:flex;gap:24px}
.footer-col{top:78px;font-size:13px;line-height:21px}
.footer-col h5{font-size:21px;font-weight:500;margin-bottom:24px}
.footer-col .gap{margin-top:8px}
.footer-rule{left:86px;top:427px;width:1028px;height:1px;background:#3a3a3a}
.copyright{left:0;top:453px;width:100%;text-align:center;font-size:13px}
</style>
</head>
<body>

<header class="site-header">
  <div class="abs brand-box"><span class="brand-name">SUMMIT MENTORS</span></div>
  <nav class="abs main-nav">
    <span>Summit Mentors</span><span>Executive Circle</span><span>For Corporations</span><span>For individuals</span>
  </nav>
  <a class="abs contact-btn">Contact</a>
</header>

<section class="hero" role="img" aria-label="Photograph of hands clapping with a burst of chalk dust on a dark background">
  <h1 class="abs hero-title">Summit mentors is an organizational consulting company</h1>
  <a class="link-underline">Learn More</a>
</section>

<section class="why">
  <h2 class="abs section-title">Why &amp; How we do it</h2>
  <p class="abs section-sub">Summit Mentors was founded in 2017 by Marco and Helena and incorporated in 2019<br>with Felix as President.</p>
  <article class="abs feature-card card-why" role="img" aria-label="Rows of colourful paper clips on a dark grey surface">
    <h3>Why we do it</h3>
    <p>We want to be instrumental in accelerating the transition to a thriving world and an enhanced level of meaning and happiness.</p>
    <span class="arrow-btn"><svg width="18" height="12" viewBox="0 0 18 12"><path d="M0 6h16M11 1l5 5-5 5" stroke="#fff" stroke-width="1.6" fill="none"/></svg></span>
  </article>
  <article class="abs feature-card card-how" role="img" aria-label="Silhouette of a climber helping another at sunset">
    <h3>How we do it</h3>
    <p>We convert the speak of purpose and consciousness into concrete solutions. We offer our services to corporations and individuals and a special series of retreats to the wider public.</p>
    <span class="arrow-btn"><svg width="18" height="12" viewBox="0 0 18 12"><path d="M0 6h16M11 1l5 5-5 5" stroke="#fff" stroke-width="1.6" fill="none"/></svg></span>
  </article>
</section>

<section class="retreats">
  <div class="abs retreats-title"><span>Retreats in Pontresina</span></div>
  <div class="abs retreat-image" role="img" aria-label="Misty alpine lake with a wooden jetty and forested mountains"></div>
  <div class="abs read-more"><a class="link-underline">Read More</a></div>
  <h2 class="abs section-title">Turn growth into thriving</h2>
  <div class="abs intro-copy">
    <p>We convert the speak of purpose and consciousness into solutions. We are deeply convinced that a life and work ethics based on the attitude of serving all stakeholders and developing high levels of inclusiveness, gratitude and consciousness would lead to more happiness and superior results for all.</p>
    <p>Our own purpose is to focus on these topics for the benefit of companies and leaders alike, thus creating an increased level of self-awareness, responsibility, fairness and alignment.</p>
    <p>Seeing leaders and companies intensely passionate for what they engage in and achieving results beyond what has been thought possible fills us with joy and gives us great fulfilment.</p>
  </div>
</section>

<section class="team">
  <h2 class="abs team-title">Meet the Team</h2>
  <p class="abs team-note">Summit Mentors was founded in 2017 by Marco and Helena and incorporated in 2019 with Felix as President.</p>

  <article class="abs member" style="left:86px" role="img" aria-label="Portrait photo of Marco Lindt">
    <div class="member-icons">
      <span><svg width="16" height="16" viewBox="0 0 24 24"><path d="M6.6 10.8a15 15 0 006.6 6.6l2.2-2.2c.3-.3.7-.4 1-.2 1.1.4 2.3.6 3.6.6.6 0 1 .4 1 1V20c0 .6-.4 1-1 1C10.6 21 3 13.4 3 4c0-.6.4-1 1-1h3.5c.6 0 1 .4 1 1 0 1.3.2 2.5.6 3.6.1.3 0 .7-.2 1z" fill="#111"/></svg></span>
      <span><svg width="16" height="12" viewBox="0 0 16 12"><rect x="1" y="1" width="14" height="10" fill="none" stroke="#111" stroke-width="1.5"/><path d="M1 1l7 6 7-6" fill="none" stroke="#111" stroke-width="1.5"/></svg></span>
      <span><svg width="16" height="16" viewBox="0 0 16 16"><circle cx="8" cy="8" r="7" fill="#111"/></svg></span>
    </div>
    <span class="role">Chief Fun Officer</span><span class="name">Marco Lindt</span>
  </article>

  <article class="abs member" style="left:437px" role="img" aria-label="Portrait photo of Dr. Felix Aregger">
    <div class="member-icons">
      <span><svg width="16" height="16" viewBox="0 0 24 24"><path d="M6.6 10.8a15 15 0 006.6 6.6l2.2-2.2c.3-.3.7-.4 1-.2 1.1.4 2.3.6 3.6.6.6 0 1 .4 1 1V20c0 .6-.4 1-1 1C10.6 21 3 13.4 3 4c0-.6.4-1 1-1h3.5c.6 0 1 .4 1 1 0 1.3.2 2.5.6 3.6.1.3 0 .7-.2 1z" fill="#111"/></svg></span>
      <span><svg width="16" height="12" viewBox="0 0 16 12"><rect x="1" y="1" width="14" height="10" fill="none" stroke="#111" stroke-width="1.5"/><path d="M1 1l7 6 7-6" fill="none" stroke="#111" stroke-width="1.5"/></svg></span>
      <span><svg width="16" height="16" viewBox="0 0 16 16"><circle cx="8" cy="8" r="7" fill="#111"/></svg></span>
    </div>
    <span class="role">Chief of Chiefs</span><span class="name">Dr. Felix Aregger</span>
  </article>

  <article class="abs member" style="left:788px" role="img" aria-label="Portrait photo of Helena Baumli">
    <div class="member-icons">
      <span><svg width="16" height="16" viewBox="0 0 24 24"><path d="M6.6 10.8a15 15 0 006.6 6.6l2.2-2.2c.3-.3.7-.4 1-.2 1.1.4 2.3.6 3.6.6.6 0 1 .4 1 1V20c0 .6-.4 1-1 1C10.6 21 3 13.4 3 4c0-.6.4-1 1-1h3.5c.6 0 1 .4 1 1 0 1.3.2 2.5.6 3.6.1.3 0 .7-.2 1z" fill="#111"/></svg></span>
      <span><svg width="16" height="12" viewBox="0 0 16 12"><rect x="1" y="1" width="14" height="10" fill="none" stroke="#111" stroke-width="1.5"/><path d="M1 1l7 6 7-6" fill="none" stroke="#111" stroke-width="1.5"/></svg></span>
      <span><svg width="16" height="16" viewBox="0 0 16 16"><circle cx="8" cy="8" r="7" fill="#111"/></svg></span>
    </div>
    <span class="role">Chief Brain Officer</span><span class="name">Helena Baumli</span>
  </article>
</section>

<section class="testimonials">
  <h2 class="abs section-title">Testimonials</h2>
  <article class="abs quote-card" style="left:86px">
    <p>A truly exceptional network of professionals from very different backgrounds who share similar values and beliefs – and, often enough, similar experiences and challenges – even though they have never met before. Exciting and enriching.</p>
    <span class="quote-author">Reto Falkner</span>
    <span class="quote-role">Chief Financial Officer, Veltria</span>
    <span class="partner-name">veltria</span>
  </article>
  <article class="abs quote-card" style="left:613px">
    <p>What impressed me is how quickly one develops trust with each other and how much one can learn from the varied paths and mindsets of participants.</p>
    <span class="quote-author">Livia Ostermann</span>
    <span class="quote-role">Alpenbank Meridian, Head Wealth Planning</span>
    <span class="partner-name" style="font-size:18px;font-weight:500">ALPENBANK MERIDIAN</span>
  </article>
</section>

<section class="media">
  <h2 class="abs section-title">Media &amp; Press</h2>
  <p class="abs section-sub">Summit Mentors was founded in 2017 by Marco and Helena and incorporated in 2019<br>with Felix as President.</p>

  <article class="abs press-card" style="left:86px">
    <div class="press-image" role="img" aria-label="Conference slide showing a panel of speakers on a dark blue background" style="background:linear-gradient(180deg,#0d1540,#18235a 60%,#0b1030)"></div>
    <span class="press-date">25 May 2021</span>
    <h4>Alpine Guild of MBAs: Digital Leaders Conference 2021</h4>
    <a class="link-underline">Read More</a>
  </article>

  <article class="abs press-card" style="left:437px">
    <div class="press-image" role="img" aria-label="Book cover and magazine spread about the first published book" style="background:linear-gradient(135deg,#f2f2f2,#c9c4bc 50%,#7d776f)"></div>
    <span class="press-date">15 September 2020</span>
    <h4>We published our first book</h4>
    <a class="link-underline">Read More</a>
  </article>

  <article class="abs press-card" style="left:788px">
    <div class="press-image" role="img" aria-label="Audience in an elegant hall listening to a speaker on stage" style="background:linear-gradient(180deg,#d8cfe0,#9b8fa6 50%,#4a3f52)"></div>
    <span class="press-date">5 April 2019</span>
    <h4>Circle of Leading Women conference 2019</h4>
    <a class="link-underline">Read More</a>
  </article>
</section>

<footer class="site-footer">
  <span class="abs footer-brand">SUMMIT MENTORS</span>
  <div class="abs footer-social">
    <svg width="18" height="18" viewBox="0 0 24 24"><path d="M6.6 10.8a15 15 0 006.6 6.6l2.2-2.2c.3-.3.7-.4 1-.2 1.1.4 2.3.6 3.6.6.6 0 1 .4 1 1V20c0 .6-.4 1-1 1C10.6 21 3 13.4 3 4c0-.6.4-1 1-1h3.5c.6 0 1 .4 1 1 0 1.3.2 2.5.6 3.6.1.3 0 .7-.2 1z" fill="#fff"/></svg>
    <svg width="20" height="18" viewBox="0 0 16 12"><rect x="1" y="1" width="14" height="10" fill="none" stroke="#fff" stroke-width="1.5"/><path d="M1 1l7 6 7-6" fill="none" stroke="#fff" stroke-width="1.5"/></svg>
    <svg width="18" height="18" viewBox="0 0 16 16"><circle cx="8" cy="8" r="7" fill="#fff"/></svg>
  </div>

  <div class="abs footer-col" style="left:410px">
    <h5>Retreats</h5>
    <div>Summit Mentors:</div>
    <div class="gap">16.03.2022 – 19.03.2022<br>08.06.2022 – 11.06.2022<br>28.09.2022 – 01.10.2022</div>
    <div class="gap">Clear Horizon Retreats</div>
    <div class="gap">02.03.2022 – 05.03.2022 (Level I)<br>14.09.2022 – 17.09.2022 (Level II)</div>
    <div class="gap">Trail to Stillness</div>
    <div class="gap">16.06.2022 – 19.06.2022</div>
  </div>

  <div class="abs footer-col" style="left:700px">
    <h5>Contact Us</h5>
    <div>Address:</div>
    <div class="gap">Summit Mentors Ltd.<br>Lindenweg 12, 8000 Zurich</div>
    <div class="gap">Telephone:</div>
    <div class="gap">+41 44 555 01 23</div>
    <div class="gap">Email:</div>
    <div class="gap">info@summitmentors-example.ch</div>
  </div>

  <div class="abs footer-col" style="left:950px">
    <h5>Quick Links</h5>
    <div>Summit Mentors</div>
    <div style="margin-top:19px">Executive Circle</div>
    <div style="margin-top:19px">For Corporations</div>
    <div style="margin-top:19px">For individuals</div>
  </div>

  <div class="abs footer-rule"></div>
  <p class="abs copyright">© Copyright &nbsp;- <strong style="font-weight:600">Summit Mentors</strong></p>
</footer>

</body>
</html>
```